Harwick Construction LTD is in need of a web page we are renovation and maintenance specialists

We are a medium size building company specialising in renovations and maintainance on commercial and residential properties bathrooms, kitchens, alterations, commercial shop fit outs, office fit outs. we also specialise in project management taking care of all manners of trades from concept to completion with trade qualified LBP registered builders customers can be assured that they will get the best possible results

Industry/Entity Type

Building

Coding

Coded - Design and coding required

Number of Pages Required

2 page

```html
<!DOCTYPE html>
<html lang="en">
<head>
<meta charset="utf-8">
<title>Harwick Construction LTD</title>
<link href="https://fonts.googleapis.com/css2?family=Open+Sans:wght@400;600;700&display=swap" rel="stylesheet">
<style>
:root{
  --navy:#1d3260;
  --navy-dark:#17284c;
  --footer:#1b2c4e;
  --ink:#2b2b2b;
  --muted:#555b66;
  --line:#d6d9de;
  --white:#ffffff;
  --panel:rgba(255,255,255,.78);
}
*{box-sizing:border-box;margin:0;padding:0}
html,body{width:778px;height:1200px;overflow:hidden}
body{font-family:"Open Sans",Arial,sans-serif;color:var(--ink);background:var(--white);position:relative}
.abs{position:absolute}

/* header */
.site-header{position:absolute;left:0;top:0;width:778px;height:104px;background:var(--white)}
.utility{position:absolute;right:40px;top:4px;display:flex;gap:6px;align-items:center}
.utility .dot{width:10px;height:10px;background:var(--navy);border-radius:2px}
.utility .search{width:62px;height:12px;background:var(--navy);margin-left:6px;font-size:6px;color:#cfd6e4;padding:1px 4px}
.brand{position:absolute;left:78px;top:30px;display:flex;align-items:center;gap:8px}
.brand .mark{width:26px;height:26px;background:var(--navy)}
.brand .name{font-weight:700;font-size:22px;color:var(--navy);letter-spacing:.5px}
.main-nav{position:absolute;right:40px;top:42px;display:flex;font-size:8.5px;font-weight:600;color:var(--navy)}
.main-nav a{padding:6px 12px;border-left:1px solid var(--line);text-decoration:none;color:inherit}
.main-nav a:first-child{border-left:none;border:1px solid var(--navy);border-bottom:2px solid var(--navy)}

/* hero */
.hero{position:absolute;left:0;top:104px;width:778px;height:259px;
  background:linear-gradient(180deg,#8fa9c9 0%,#5b7aa3 35%,#2f4670 70%,#1c2a48 100%)}
.hero-line{position:absolute;background:var(--panel);color:#22314f}
.hero-line.one{left:135px;top:64px;width:295px;height:50px;font-size:28px;padding:7px 14px}
.hero-line.two{left:140px;top:124px;width:235px;height:36px;font-size:19px;font-weight:700;padding:5px 12px}
.hero-line.three{left:140px;top:168px;width:300px;height:36px;font-size:19px;padding:5px 12px}
.hero-arrows{position:absolute;right:85px;top:228px;display:flex;gap:3px}
.hero-arrows span{width:13px;height:13px;background:var(--white);display:flex;align-items:center;justify-content:center}

/* welcome */
.welcome{position:absolute;left:60px;top:383px;width:658px;text-align:center}
.welcome h1{font-size:12px;font-weight:700;color:#1f2b44;margin-bottom:5px}
.welcome p{font-size:8px;line-height:12.5px;color:var(--muted)}

/* services */
.service{position:absolute;top:478px;width:190px;text-align:center}
.service h2{font-size:11.5px;font-weight:700;color:#1f2b44;margin-bottom:8px}
.service svg{display:block;margin:0 auto}
.service p{font-size:8px;line-height:12px;color:var(--muted);margin-top:8px}

/* latest project */
.latest{position:absolute;left:0;top:669px;width:778px;height:161px;
  background:linear-gradient(180deg,#3b5a8c 0%,#2b4a7c 50%,#223e6c 100%);text-align:center;color:var(--white)}
.latest h2{font-size:12px;font-weight:700;margin-top:56px}
.latest h2::after{content:"";display:block;width:44px;height:2px;background:var(--white);margin:3px auto 0}
.latest p{font-size:8px;line-height:12.5px;width:640px;margin:8px auto 0;color:#e4e9f2}
.btn{display:inline-block;margin-top:10px;background:var(--white);color:var(--navy);font-size:8.5px;font-weight:700;padding:4px 12px;border-radius:3px}

/* team */
.team-title{position:absolute;left:0;top:868px;width:778px;text-align:center;font-size:12px;font-weight:700;color:#1f2b44}
.team-title::after{content:"";display:block;width:44px;height:2px;background:var(--navy);margin:3px auto 0}
.member{position:absolute;top:907px;width:104px;height:118px;background:linear-gradient(180deg,#eef0f3,#c9ced6)}
.carousel-btn{position:absolute;top:950px;width:34px;height:34px;border-radius:50%;background:var(--white);box-shadow:0 1px 4px rgba(0,0,0,.35);display:flex;align-items:center;justify-content:center}

/* footer */
.site-footer{position:absolute;left:0;top:1063px;width:778px;height:137px;background:var(--footer);color:var(--white)}
.f-col{position:absolute;top:12px}
.f-col h3{font-size:10px;font-weight:700;margin-bottom:6px}
.f-col ul{list-style:none;font-size:6.5px;line-height:11px;color:#d4dbe8}
.f-col li{display:flex;align-items:center;gap:5px}
.f-social{display:flex;gap:5px;margin-top:2px}
.f-social span{width:13px;height:13px;background:#3a4f78}
.f-col p{font-size:6.5px;color:#d4dbe8;margin-bottom:6px}
.subscribe{display:flex}
.subscribe .field{width:140px;height:16px;background:var(--white);font-size:6px;color:#888;padding:4px}
.subscribe .go{width:44px;height:16px;background:#2f4673;font-size:6px;padding:4px;text-align:center}
.f-brand{position:absolute;left:560px;top:86px;display:flex;align-items:center;gap:6px}
.f-brand .mark{width:16px;height:16px;background:var(--white)}
.f-brand .name{font-weight:700;font-size:15px;color:var(--white)}
</style>
</head>
<body>

<header class="site-header">
  <div class="utility"><span class="dot"></span><span class="dot"></span><span class="dot"></span><span class="dot"></span><span class="search">Search</span></div>
  <div class="brand"><span class="mark"></span><span class="name">Harwick Construction</span></div>
  <nav class="main-nav">
    <a>HOME</a><a>ABOUT</a><a>SERVICES</a><a>PROJECTS</a><a>TEAM</a><a>CONTACT US</a>
  </nav>
</header>

<section class="hero" role="img" aria-label="Dusk photograph of a city skyline with high-rise towers">
  <div class="hero-line one">Welcome to Archit</div>
  <div class="hero-line two">Architecture Studio</div>
  <div class="hero-line three">Architecture Inferior Designs</div>
  <div class="hero-arrows">
    <span><svg width="6" height="8" viewBox="0 0 6 8"><path d="M5 0L1 4l4 4" fill="none" stroke="#1d3260" stroke-width="1.5"/></svg></span>
    <span><svg width="6" height="8" viewBox="0 0 6 8"><path d="M1 0l4 4-4 4" fill="none" stroke="#1d3260" stroke-width="1.5"/></svg></span>
  </div>
</section>

<section class="welcome">
  <h1>WELCOME TO HARWICK CONSTRUCTION LTD.</h1>
  <p>We are a medium size building company specialising in renovations and maintenance on commercial and residential properties, from bathrooms and kitchens to alterations, shop fit outs and office fit outs. We also manage projects across all trades from concept to completion. With trade qualified LBP registered builders on every job, our customers can be assured of the best possible results, delivered on time and on budget by a team that cares about quality.</p>
</section>

<section class="service" style="left:45px">
  <h2>Architecture</h2>
  <svg width="80" height="80" viewBox="0 0 80 80"><polygon points="24,2 56,2 78,24 78,56 56,78 24,78 2,56 2,24" fill="#1d3260"/><path d="M28 54L52 26M30 30h10v10" stroke="#fff" stroke-width="3" fill="none"/></svg>
  <p>Lorem ipsum dolor sit amet,<br>consectetur adipiscing elit.</p>
</section>
<section class="service" style="left:293px">
  <h2>Project Management</h2>
  <svg width="80" height="80" viewBox="0 0 80 80"><polygon points="24,2 56,2 78,24 78,56 56,78 24,78 2,56 2,24" fill="#1d3260"/><circle cx="28" cy="40" r="6" fill="#fff"/><circle cx="52" cy="28" r="5" fill="#fff"/><circle cx="52" cy="52" r="5" fill="#fff"/><path d="M28 40L52 28M28 40L52 52" stroke="#fff" stroke-width="2.5"/></svg>
  <p>Lorem ipsum dolor sit amet,<br>consectetur adipiscing elit.</p>
</section>
<section class="service" style="left:541px">
  <h2>Research</h2>
  <svg width="80" height="80" viewBox="0 0 80 80"><polygon points="24,2 56,2 78,24 78,56 56,78 24,78 2,56 2,24" fill="#1d3260"/><circle cx="36" cy="36" r="11" fill="none" stroke="#fff" stroke-width="3.5"/><path d="M44 44l12 12" stroke="#fff" stroke-width="5" stroke-linecap="round"/></svg>
  <p>Lorem ipsum dolor sit amet,<br>consectetur adipiscing elit.</p>
</section>

<section class="latest" role="img" aria-label="Blue-tinted photograph of city towers behind the latest project text">
  <h2>Latest Project</h2>
  <p>A full office fit out for a busy city client, completed in stages so the team could keep working throughout. New partitions, ceilings, lighting and a modern kitchen were delivered by our own registered builders and trusted trades, on time and within the agreed budget.</p>
  <span class="btn">Click Here</span>
</section>

<h2 class="team-title">Meet the Team</h2>
<div class="carousel-btn" style="left:90px"><svg width="8" height="12" viewBox="0 0 8 12"><path d="M6 1L1 6l5 5" fill="none" stroke="#1d3260" stroke-width="2"/></svg></div>
<div class="member" role="img" aria-label="Portrait of a team member" style="left:150px"></div>
<div class="member" role="img" aria-label="Portrait of a team member" style="left:272px"></div>
<div class="member" role="img" aria-label="Portrait of a team member" style="left:394px"></div>
<div class="member" role="img" aria-label="Portrait of a team member" style="left:516px"></div>
<div class="carousel-btn" style="left:654px"><svg width="8" height="12" viewBox="0 0 8 12"><path d="M2 1l5 5-5 5" fill="none" stroke="#1d3260" stroke-width="2"/></svg></div>

<footer class="site-footer">
  <div class="f-col" style="left:85px">
    <h3>Navigation</h3>
    <ul><li>HOME</li><li>ABOUT</li><li>SERVICES</li><li>PROJECTS</li><li>TEAM</li><li>CONTACT US</li></ul>
  </div>
  <div class="f-col" style="left:228px">
    <h3>Our Location</h3>
    <ul>
      <li><svg width="7" height="9" viewBox="0 0 7 9"><path d="M3.5 9S0 5 0 3.5a3.5 3.5 0 017 0C7 5 3.5 9 3.5 9z" fill="#fff"/></svg>14 Kestrel Road,<br>Northvale 4021</li>
      <li><svg width="7" height="7" viewBox="0 0 7 7"><rect x="1.5" y="0" width="4" height="7" rx="1" fill="#fff"/></svg>+1 555 014 2280</li>
      <li><svg width="7" height="7" viewBox="0 0 7 7"><rect x="1.5" y="0" width="4" height="7" rx="1" fill="#fff"/></svg>+1 555 014 2281</li>
      <li><svg width="8" height="6" viewBox="0 0 8 6"><rect width="8" height="6" fill="#fff"/><path d="M0 0l4 3 4-3" stroke="#1b2c4e" fill="none"/></svg>office@harwickbuild.example</li>
    </ul>
  </div>
  <div class="f-col" style="left:368px">
    <h3>Follow us</h3>
    <div class="f-social"><span></span><span></span><span></span><span></span></div>
  </div>
  <div class="f-col" style="left:505px">
    <h3>Subscribe Newsletter</h3>
    <p>Get project news sent straight to your inbox</p>
    <div class="subscribe"><span class="field">Enter Your Email Address</span><span class="go">Subscribe</span></div>
  </div>
  <div class="f-brand"><span class="mark"></span><span class="name">Harwick Construction</span></div>
</footer>

</body>
</html>
```